Hot-air ballooning company needs a DL-size flyer

Skylark Aerial Tours is a hot-air ballooning company which flies passengers in the King Valley, Victoria, Australia.
We need a 2-sided DL-size flyer which promotes our hot-air balloon flights and packages.
Most of our customers are couples, and we want the flyer design to communicate safety, adventure, and romance.
The flyer should make the best use of our images which we provide, and we've also included a document with the text for the flyer.
Updates

2 days is not long enough to gather designs, the brief never asked me what my deadline should be.

Target Market(s)

Couples, buyers are majority female, between the ages of 20-60

Industry/Entity Type

Tourism

Font styles to use
Sans Serif

Colors

Designer to choose colors to be used in the design.

Requirements
Must have
• Communicate safety, adventure, and romance
• Use images
Nice to have
• There is a lot of text, it would be great if you could make it look like as little text as possible
Should not have
• No childish designs

```html
<!DOCTYPE html>
<html lang="en">
<head>
<meta charset="utf-8">
<title>Skylark Aerial Tours – DL Flyer</title>
<link rel="stylesheet" href="https://fonts.googleapis.com/css2?family=Oswald:wght@500;600&family=Open+Sans:ital,wght@0,400;0,600;0,700;1,400;1,700;1,800&display=swap">
<style>
:root{
  --backdrop:#3a3a3a;
  --red:#c4121a;
  --red-deep:#a10d14;
  --ink:#111111;
  --text:#222222;
  --paper:#ffffff;
}
*{box-sizing:border-box;margin:0;padding:0}
html,body{width:900px;height:1200px;overflow:hidden}
body{background:var(--backdrop);font-family:"Open Sans",Arial,sans-serif;color:var(--text);position:relative}
.panel{position:absolute;background:var(--paper);overflow:hidden}
.front{left:62px;top:182px;width:388px;height:775px}
.back{left:487px;top:182px;width:385px;height:770px}

.photo{position:absolute}
.ph-basket{left:0;top:4px;width:178px;height:132px;
  background:radial-gradient(ellipse 60% 45% at 55% 18%,#3a2e26 0%,#3a2e26 60%,transparent 62%),
             linear-gradient(180deg,#9fc1e0 0%,#c9b98a 45%,#d98f2e 62%,#5f7a3c 82%,#3d4a2a 100%)}
.ph-valley{left:191px;top:0;width:197px;height:170px;
  background:linear-gradient(180deg,#2f78d2 0%,#5c9ce0 45%,#a9c7e4 63%,#c8d2d8 72%,#7f8a8c 82%,#3c4540 100%)}
.ph-vineyard{left:0;top:141px;width:185px;height:143px;
  background:linear-gradient(180deg,#3f88d8 0%,#8fbbe3 30%,#d6dee6 42%,#7f8c66 58%,#4c5a34 75%,#3b2f24 100%)}
.ph-sunrise{left:0;top:288px;width:203px;height:136px;
  background:linear-gradient(180deg,#2e74cc 0%,#6aa3de 40%,#b9cfe2 62%,#9a9a88 74%,#5d5f48 88%,#3c3d2e 100%)}
.couple-bg{position:absolute;left:263px;top:283px;width:125px;height:141px;background:var(--red)}
.ph-couple{left:206px;top:256px;width:182px;height:168px;
  background:radial-gradient(ellipse 70% 80% at 55% 45%,#e2b9a2 0%,#c38e76 45%,transparent 72%),
             linear-gradient(180deg,transparent 0%,transparent 70%,#d8d6d4 100%)}

.title{position:absolute;left:198px;top:190px;width:190px;text-align:center;font-family:"Oswald",Arial,sans-serif;line-height:1}
.title .t1{display:block;color:var(--red);font-size:29px;font-weight:600;letter-spacing:.3px}
.title .t2{display:block;color:var(--ink);font-size:17px;font-weight:500;margin-top:4px}
.band{position:absolute;left:0;top:434px;width:388px;height:31px;background:var(--ink);color:var(--paper);font-family:"Oswald",Arial,sans-serif;font-weight:500;font-size:15px;text-align:center;line-height:31px;letter-spacing:.2px}
.intro{position:absolute;left:26px;top:473px;width:345px;font-family:Arial,sans-serif;font-size:12.4px;font-weight:700;line-height:15px;color:var(--ink)}
.faded{position:absolute;left:0;top:520px;width:388px;height:228px;background:linear-gradient(180deg,#ffffff 0%,#f1f1f1 45%,#d4d4d4 100%)}

.points{list-style:none}
.points li{position:absolute;font-style:italic;font-size:10.8px;line-height:14.8px;color:var(--text)}
.icon{position:absolute;width:20px;height:24px}
.front .points li{left:66px;width:292px;text-align:justify;text-align-last:left}
.front .icon{left:-42px}
.back .points li{font-size:10.6px;line-height:14.8px}
.back .icon{left:-29px}

.foot{position:absolute;left:0;bottom:0;width:100%;height:27px}
.foot .left,.foot .right{position:absolute;top:0;height:27px;font-style:italic;font-weight:700;font-size:8.6px;line-height:27px;color:var(--paper)}

.hero{position:absolute;left:0;top:0;width:385px;height:300px;
  background:radial-gradient(ellipse 38% 55% at 78% 28%,#f6c23a 0%,#ef8a2a 45%,transparent 75%),
             radial-gradient(ellipse 40% 50% at 18% 22%,#e83b2a 0%,#f0a132 50%,transparent 78%),
             linear-gradient(180deg,#d2402c 0%,#f2a531 30%,#6e7578 58%,#2f3a40 72%,#7b8589 86%,#ffffff 100%)}
.flight-title{position:absolute;left:0;top:296px;width:100%;text-align:center;font-style:italic;font-weight:800;font-size:35px;letter-spacing:-.5px;color:var(--ink)}
.flight-title em{color:var(--red);font-style:italic}

.contact{position:absolute;left:206px;top:503px;width:159px;height:212px;border:2px solid var(--ink);border-radius:10px;text-align:center;background:var(--paper)}
.contact .tab{position:absolute;left:12px;top:-12px;width:135px;height:28px;background:linear-gradient(180deg,#d91a22,var(--red-deep));border-radius:12px 12px 0 0;color:var(--paper);font-style:italic;font-weight:700;font-size:13px;line-height:28px}
.contact .call{margin-top:28px;font-style:italic;font-weight:800;font-size:16px;line-height:18px;color:var(--ink)}
.contact .small{font-weight:700;font-style:italic;font-size:9.4px;line-height:12.5px;color:var(--ink);margin-top:8px;padding:0 6px}
</style>
</head>
<body>
<svg width="0" height="0" style="position:absolute">
  <defs>
    <symbol id="balloon" viewBox="0 0 20 24">
      <path d="M10 1 C4.5 1 1.5 5 1.5 9.5 C1.5 13.5 5 16.5 7 18 L13 18 C15 16.5 18.5 13.5 18.5 9.5 C18.5 5 15.5 1 10 1Z" fill="none" stroke="#c4121a" stroke-width="1.6"/>
      <path d="M10 1.5 C6.5 4 6 12 8 18 M10 1.5 C13.5 4 14 12 12 18" fill="none" stroke="#c4121a" stroke-width="1.3"/>
      <path d="M7.5 18 L8.5 20.5 M12.5 18 L11.5 20.5" stroke="#c4121a" stroke-width="1"/>
      <rect x="8" y="20.5" width="4" height="3" fill="#c4121a"/>
    </symbol>
  </defs>
</svg>

<section class="panel front" aria-label="Flyer front">
  <div class="photo ph-basket" role="img" aria-label="Balloon basket with passengers above a river at sunrise"></div>
  <div class="photo ph-valley" role="img" aria-label="Striped hot-air balloon over a misty valley"></div>
  <div class="photo ph-vineyard" role="img" aria-label="Balloons drifting over vineyards and fields"></div>
  <div class="photo ph-sunrise" role="img" aria-label="Rainbow balloon rising over countryside at dawn"></div>
  <div class="couple-bg"></div>
  <div class="photo ph-couple" role="img" aria-label="Smiling couple embracing"></div>
  <h1 class="title"><span class="t1">KING VALLEY</span><span class="t2">HOT-AIR BALLOONING</span></h1>
  <div class="band">THE PERFECT GOURMET BALLOONING EXPERIENCE</div>
  <p class="intro">Live the romance and adventure of flying the beautiful King Valley and surrounds in a hot-air balloon at dawn</p>
  <div class="faded" role="img" aria-label="Faded landscape with balloons"></div>
  <ul class="points">
    <li style="top:527px"><svg class="icon" style="top:3px"><use href="#balloon"/></svg>The mountain views, once aloft, come to life in dramatic 3D with the early morning light</li>
    <li style="top:571px"><svg class="icon" style="top:4px"><use href="#balloon"/></svg>From the vineyards and patchwork of fields the views expand to the Ovens River, spectacular Mt Buffalo and the High Country beyond</li>
    <li style="top:626px"><svg class="icon" style="top:3px"><use href="#balloon"/></svg>Celebrate your flight with a delicious breakfast afterwards (optional)</li>
    <li style="top:671px"><svg class="icon" style="top:4px"><use href="#balloon"/></svg>Milawa is conveniently located less than an hour's drive from most places in Victoria's North East and Albury in NSW Mansfield flights are also available</li>
  </ul>
  <div class="foot">
    <svg width="388" height="27" style="position:absolute;left:0;top:0">
      <rect width="388" height="27" fill="#111111"/>
      <polygon points="0,0 255,0 266,27 0,27" fill="#a10d14"/>
    </svg>
  </div>
</section>

<section class="panel back" aria-label="Flyer back">
  <div class="hero" role="img" aria-label="Glowing hot-air balloons being inflated with a crowd watching at dawn"></div>
  <h2 class="flight-title"><em>YOUR</em> FLIGHT</h2>
  <ul class="points">
    <li style="left:44px;top:350px;width:140px"><svg class="icon" style="top:12px"><use href="#balloon"/></svg>One-hour sunrise balloon flight in the spectacular King Valley region in North East Victoria</li>
    <li style="left:44px;top:424px;width:140px"><svg class="icon" style="top:10px"><use href="#balloon"/></svg>Delicious champagne breakfast after the flight (recommended option)</li>
    <li style="left:40px;top:492px;width:160px"><svg class="icon" style="top:-4px"><use href="#balloon"/></svg>Safe, friendly and professional</li>
    <li style="left:40px;top:522px;width:160px"><svg class="icon" style="top:2px"><use href="#balloon"/></svg>The flight lasts approximately 1 hour</li>
    <li style="left:40px;top:566px;width:160px"><svg class="icon" style="top:-1px"><use href="#balloon"/></svg>The entire experience takes about 3-4 hours</li>
    <li style="left:40px;top:611px;width:160px"><svg class="icon" style="top:-4px"><use href="#balloon"/></svg>Suitable from age 7 to 97</li>
    <li style="left:40px;top:641px;width:160px"><svg class="icon" style="top:-4px"><use href="#balloon"/></svg>Gift Vouchers are also available</li>
    <li style="left:40px;top:670px;width:160px"><svg class="icon" style="top:2px"><use href="#balloon"/></svg>Contact us for exclusive flight options at your custom location</li>
    <li style="left:242px;top:350px;width:122px"><svg class="icon" style="top:5px"><use href="#balloon"/></svg>informative details throughout your experi-ence with our locally based expert crew</li>
    <li style="left:242px;top:424px;width:122px"><svg class="icon" style="top:11px"><use href="#balloon"/></svg>The opportunity to be involved in the inflation and deflation process should you wish</li>
  </ul>
  <div class="contact">
    <div class="tab">contact details</div>
    <p class="call">CALL US TODAY<br>1300 555 014</p>
    <p class="small">Find us also on social media and travel review sites @skylarkaerialtours</p>
    <p class="small">Skylark Aerial Tours operates under Air Operator's Certificate C481207-15</p>
    <p class="small">issued by the National Air Safety Regulator</p>
  </div>
  <div class="foot">
    <svg width="385" height="27" style="position:absolute;left:0;top:0">
      <rect width="385" height="27" fill="#a10d14"/>
      <polygon points="0,0 181,0 192,27 0,27" fill="#111111"/>
    </svg>
    <span class="left" style="left:14px">visit-www.skylarkaerialtours.com.au</span>
    <span class="right" style="right:8px">mail-flights@skylarkaerialtours.com.au</span>
  </div>
</section>
</body>
</html>
```